Eye catching Stationary Design

Healthcare consultant firm looking for stationary design ( letterhead, envelope and business cards) That’s professional, classy and eye catching . The design should incorporate the logo and the colors of the logo in its design. You can see the logo on our website at www crestmore advisory. net.

```html
<!DOCTYPE html>
<html lang="en">
<head>
<meta charset="utf-8">
<title>Crestmore Advisory – Letterhead</title>
<link rel="stylesheet" href="https://fonts.googleapis.com/css2?family=Source+Sans+3:wght@400;600&family=Great+Vibes&display=swap">
<style>
  :root {
    --backdrop: #d8d8da;
    --paper: #ffffff;
    --paper-shade: #f1f2f4;
    --ink: #555659;
    --ink-dark: #2b2b2d;
    --brand-blue: #0f5aa8;
    --rule-blue: #2aa3dc;
    --deco-warm: #f7c9c0;
    --deco-mid: #f3e6b8;
    --deco-cool: #cfe9f2;
  }
  * { box-sizing: border-box; margin: 0; padding: 0; }
  html, body {
    width: 1200px; height: 1113px; overflow: hidden;
    background: var(--backdrop);
  }
  .letterhead {
    position: absolute; left: 222px; top: 26px;
    width: 755px; height: 1060px;
    background: linear-gradient(160deg, var(--paper) 35%, var(--paper-shade) 100%);
    font-family: "Source Sans 3", "Helvetica Neue", Arial, sans-serif;
    color: var(--ink);
    overflow: hidden;
  }
  .brand {
    position: absolute; top: 58px; left: 0; width: 100%;
    display: flex; justify-content: center; align-items: center; gap: 10px;
  }
  .brand-dot { width: 14px; height: 14px; border-radius: 50%; background: var(--brand-blue); }
  .brand-name {
    font-size: 22px; font-weight: 600; letter-spacing: 2px;
    text-transform: uppercase; color: var(--brand-blue);
  }
  .background-art {
    position: absolute; left: 48px; top: 300px; width: 640px; height: 560px;
    opacity: 0.55;
  }
  .letter-body {
    position: absolute; left: 63px; top: 274px; width: 628px;
  }
  .salutation { font-size: 14px; margin-bottom: 18px; }
  .paragraph {
    font-size: 14px; line-height: 24px; text-align: justify;
    margin-bottom: 18px;
  }
  .closing { font-size: 17px; margin-top: 24px; }
  .signature {
    font-family: "Great Vibes", cursive;
    font-size: 34px; color: var(--brand-blue); margin-top: 2px;
  }
  .footer { position: absolute; left: 0; top: 984px; width: 100%; font-size: 10.5px; color: var(--ink-dark); }
  .footer-address { display: flex; justify-content: center; align-items: center; gap: 6px; }
  .footer-rule { margin: 9px auto 11px; width: 591px; height: 2px; background: var(--rule-blue); }
  .footer-contacts { display: flex; justify-content: center; align-items: center; gap: 12px; }
  .contact { display: flex; align-items: center; gap: 6px; }
  .icon { width: 11px; height: 11px; }
</style>
</head>
<body>
  <main class="letterhead">
    <header class="brand">
      <span class="brand-dot"></span>
      <span class="brand-name">Crestmore Advisory LLC</span>
    </header>

    <svg class="background-art" role="img" aria-label="Faint decorative network globe with scattered pastel squares" viewBox="0 0 640 560">
      <defs>
        <linearGradient id="globe-tone" x1="0" y1="0" x2="0" y2="1">
          <stop offset="0" stop-color="#f7c9c0"/>
          <stop offset="0.5" stop-color="#f3e6b8"/>
          <stop offset="1" stop-color="#cfe9f2"/>
        </linearGradient>
        <linearGradient id="square-tone" x1="0" y1="0" x2="0" y2="1">
          <stop offset="0" stop-color="#f7d3cc"/>
          <stop offset="1" stop-color="#e2efd6"/>
        </linearGradient>
      </defs>
      <circle cx="248" cy="308" r="248" fill="url(#globe-tone)" opacity="0.45"/>
      <rect x="430" y="10" width="210" height="470" rx="30" fill="url(#square-tone)" opacity="0.4"/>
    </svg>

    <section class="letter-body">
      <p class="salutation">Dear Mr. Lorem,</p>
      <p class="paragraph">Lorem ipsum dolor sit amet, consectetuer adipiscing elit, sed diam nonummy nibh euismod tincidunt ut laoreet dolore magna aliquam erat volutpat. Ut wisi enim ad minim veniam, quis nostrud exerci tation ullamcorper suscipit lobortis nisl ut aliquip ex ea commodo consequat. Duis autem vel eum iriure dolor in hendiusto odio dignissim qui blandit praesent luptatum zzril delenit augue duis dolore te feugait nulla facilisi.</p>
      <p class="paragraph">Lorem ipsum dolor sit amet, consectetuer adipiscing elit, sed diam nonummy nibh euismod tincidunt ut laoreet dolore magna aliquam erat volutpat. Ut wisi enim ad minim veniam, quis nostrud exerci tation ullamcorper suscipit lobortis nisl ut aliquip ex ea commodo consequat. Duis autem vel eum iriure dolor in hendiusto odio dignissim qui blandit praesent luptatum zzril delenit augue duis dolore te feugait nulla facilisi.</p>
      <p class="paragraph">Lorem ipsum dolor sit amet, consectetuer adipiscing elit, sed diam nonummy nibh euismod tincidunt ut laoreet dolore magna aliquam erat volutpat. Ut wisi enim ad minim veniam, quis nostrud exerci tation ullamcorper suscipit lobortis nisl ut aliquip ex ea commodo consequat. Duis autem vel eum iriure dolor in hendiusto odio dignissim qui blandit praesent luptatum zzril delenit augue duis dolore te feugait nulla facilisi.</p>
      <p class="closing">Sincerely Your,</p>
      <p class="signature">Your Name</p>
    </section>

    <footer class="footer">
      <div class="footer-address">
        <svg class="icon" viewBox="0 0 12 12"><path d="M6 1a3.5 3.5 0 0 0-3.5 3.5C2.5 7 6 11 6 11s3.5-4 3.5-6.5A3.5 3.5 0 0 0 6 1z" fill="none" stroke="#2aa3dc" stroke-width="1.3"/><circle cx="6" cy="4.5" r="1.2" fill="#2aa3dc"/></svg>
        <span>118 Harbor Lane Suite 40, Portland, OR 97205, USA</span>
      </div>
      <div class="footer-rule"></div>
      <div class="footer-contacts">
        <span class="contact">
          <svg class="icon" viewBox="0 0 12 12"><path d="M2.5 1.5l2 .3.8 2.3-1.2 1a6 6 0 0 0 2.8 2.8l1-1.2 2.3.8.3 2c-4.5.6-8.6-3.5-8-8z" fill="#2aa3dc"/></svg>
          (503) 555-0148
        </span>
        <span class="contact">
          <svg class="icon" viewBox="0 0 12 12"><rect x="1" y="2.5" width="10" height="7" fill="#2aa3dc"/><path d="M1 2.5l5 4 5-4" fill="none" stroke="#fff" stroke-width="1"/></svg>
          info@crestmoreadvisory.net
        </span>
        <span class="contact">
          <svg class="icon" viewBox="0 0 12 12"><circle cx="6" cy="6" r="5" fill="none" stroke="#2aa3dc" stroke-width="1.1"/><ellipse cx="6" cy="6" rx="2.2" ry="5" fill="none" stroke="#2aa3dc" stroke-width="0.9"/><path d="M1 6h10" stroke="#2aa3dc" stroke-width="0.9"/></svg>
          www.crestmoreadvisory.net
        </span>
      </div>
    </footer>
  </main>
</body>
</html>
```